Data Visualization (graphs, tables, models, circles)

We need an intuitive - user friendly - and fresh design line for our data visualization.

You know. Keep The Page Calm!

Our core product is based on the presentation and interpretation of different data sources that we combine into graphs, tables, charts etc and make visible to clients through a web platform and or Reports. Our business area is Search & Social Media Intelligence.

See Vantrel.com for some inspiration in terms of current colors and a better understanding of the company. Our Logo / Name is the only one thing that cannot be changed. Everything else is up to you. Feel free to ask questions.

I have attached a few screenshots of some of our features and as you can see - there has never been a designer on this assignment. We are looking for a long term relationship with a designer that can work with us on an ongoing basis.

Design of graphs/models/circles/tables needs to be able to fit into Infographics also.

We are basically looking for an identity for our data visualization. Meaning that readers / target audience can recognize our graphs and say: Check out the cool graphs by Vantrel :-)

Think: Plorvex, TallyNorth, etc. in terms of data presentation.
Updates

Project Deadline Extended
Reason: Due to illness we lost a few days last week and have not have sufficient time to look through the different designs.

Target Market(s)

Marketing People, CEO's, Strategic Planners, Ad Agencies, Decision Makers

Industry/Entity Type

Business

Requirements
Must have
• Must present at least 1 line graph (like file 1 and 2), 1 pie chart, 1 column graph and 1 matrix (like file3).

```html
<!DOCTYPE html>
<html lang="en">
<head>
<meta charset="utf-8">
<title>Vantrel – Data Visualization</title>
<link rel="stylesheet" href="https://fonts.googleapis.com/css2?family=Tinos&family=Carlito:wght@400&display=swap">
<style>
  :root {
    --green: #6b8e1f;
    --green-dark: #4f6b14;
    --red: #991217;
    --red-dark: #6e0c10;
    --blue: #1f7494;
    --blue-dark: #165870;
    --purple: #b41fe0;
    --orange: #ff8a00;
    --title-blue: #0000ff;
    --ink: #000;
    --brand: #8e1218;
    --bg-light: #ffffff;
    --bg-grey: #e4e4e4;
  }
  html, body { margin: 0; padding: 0; overflow: hidden; background: var(--bg-light); }
  .canvas { display: block; width: 1200px; height: 900px; }
  .panel-title { font-family: "Tinos", "Times New Roman", serif; font-size: 46px; fill: var(--ink); }
  .panel-title .accent { fill: var(--title-blue); }
  .brand-name { font-family: "Carlito", "Calibri", sans-serif; font-size: 84px; fill: var(--brand); }
  .brand-faint { font-family: "Carlito", "Calibri", sans-serif; font-size: 430px; fill: var(--brand); opacity: .13; }
  .axis-text { font-family: "Carlito", "Verdana", sans-serif; font-size: 9px; fill: var(--ink); }
  .axis-small { font-family: "Carlito", "Verdana", sans-serif; font-size: 8px; fill: var(--ink); }
  .legend-text { font-family: "Carlito", "Calibri", sans-serif; font-size: 15px; fill: var(--ink); }
  .pie-label { font-family: "Carlito", "Calibri", sans-serif; font-size: 14px; fill: #fff; }
  .pie-label.outside { fill: var(--ink); }
  .axis-line { stroke: var(--ink); stroke-width: 1; fill: none; }
  .series { fill: none; stroke-width: 2.6; stroke-linejoin: round; }
  .series-yours { stroke: var(--green); }
  .series-c1 { stroke: var(--red); }
  .series-c2 { stroke: var(--blue); }
  .fill-green { fill: var(--green); }
  .fill-red { fill: var(--red); }
  .fill-blue { fill: var(--blue); }
  .fill-purple { fill: var(--purple); }
  .fill-orange { fill: var(--orange); }
</style>
</head>
<body>
<svg class="canvas" viewBox="0 0 1200 900" xmlns="http://www.w3.org/2000/svg">
  <defs>
    <radialGradient id="backdrop" cx="50%" cy="45%" r="75%">
      <stop offset="0" stop-color="#ffffff"/>
      <stop offset="0.6" stop-color="#f3f3f3"/>
      <stop offset="1" stop-color="#dcdcdc"/>
    </radialGradient>
  </defs>

  <rect role="img" aria-label="Soft grey background with faint sweeping curves" width="1200" height="900" fill="url(#backdrop)"/>

  <text class="brand-faint" x="105" y="790">vantrel</text>
  <text class="brand-name" x="660" y="95" text-anchor="middle">Vantrel</text>

  <!-- A. Column graph -->
  <g class="chart-column">
    <text class="panel-title" x="115" y="125">A. <tspan class="accent">Column Graph</tspan></text>
    <text class="axis-small" x="43" y="108">Your</text>
    <text class="axis-small" x="43" y="118">Returns</text>
    <text class="axis-small" x="43" y="128">(€. million.)</text>
    <path class="axis-line" d="M80 142 V426 H680"/>
    <g class="axis-small" text-anchor="end">
      <text x="70" y="429">0</text><text x="70" y="401">1</text><text x="70" y="372">2</text>
      <text x="70" y="344">3</text><text x="70" y="315">4</text><text x="70" y="287">5</text>
      <text x="70" y="259">6</text><text x="70" y="230">7</text><text x="70" y="202">8</text>
      <text x="70" y="173">9</text><text x="70" y="145">10</text>
    </g>
    <g class="fill-green">
      <rect x="91" y="190.3" width="18" height="235.7"/>
      <rect x="140" y="180.3" width="18" height="245.7"/>
      <rect x="188" y="363.5" width="18" height="62.5"/>
      <rect x="239" y="264.1" width="18" height="161.9"/>
      <rect x="288" y="210.2" width="18" height="215.8"/>
      <rect x="335" y="298.2" width="18" height="127.8"/>
      <rect x="386" y="282.6" width="18" height="143.4"/>
      <rect x="434" y="380.6" width="18" height="45.4"/>
      <rect x="482" y="345.1" width="18" height="80.9"/>
      <rect x="532" y="151.9" width="18" height="274.1"/>
      <rect x="582" y="296.8" width="18" height="129.2"/>
      <rect x="629" y="281.2" width="18" height="144.8"/>
    </g>
    <g class="axis-small" text-anchor="middle">
      <text x="100" y="440">January</text><text x="149" y="440">February</text>
      <text x="197" y="440">March</text><text x="248" y="440">April</text>
      <text x="297" y="440">May</text><text x="344" y="440">June</text>
      <text x="395" y="440">July</text><text x="443" y="440">August</text>
      <text x="497" y="440">September</text><text x="541" y="440">October</text>
      <text x="591" y="440">November</text><text x="638" y="440">December</text>
      <text x="395" y="453">Months (year 2012)</text>
    </g>
  </g>

  <!-- B. Share -->
  <g class="chart-share">
    <text class="panel-title" x="948" y="125">B. <tspan class="accent">Share</tspan></text>
    <path fill="var(--green-dark)" d="M1165 228 A130 78 0 0 1 1158.6 252.1 L1158.6 280.1 A130 78 0 0 0 1165 256 Z"/>
    <path fill="var(--red)" d="M1158.6 252.1 A130 78 0 0 1 972 296.2 L972 324.2 A130 78 0 0 0 1158.6 280.1 Z"/>
    <path fill="var(--purple)" d="M972 296.2 A130 78 0 0 1 958.6 291.1 L958.6 319.1 A130 78 0 0 0 972 324.2 Z"/>
    <path fill="var(--blue-dark)" d="M958.6 291.1 A130 78 0 0 1 905 228 L905 256 A130 78 0 0 0 958.6 319.1 Z"/>
    <path class="fill-green" d="M1035 228 L1035 150 A130 78 0 0 1 1158.6 252.1 Z"/>
    <path class="fill-red" d="M1035 228 L1158.6 252.1 A130 78 0 0 1 972 296.2 Z"/>
    <path class="fill-purple" d="M1035 228 L972 296.2 A130 78 0 0 1 958.6 291.1 Z"/>
    <path class="fill-blue" d="M1035 228 L958.6 291.1 A130 78 0 0 1 946.3 171 Z"/>
    <path class="fill-orange" d="M1035 228 L946.3 171 A130 78 0 0 1 1035 150 Z"/>
    <text class="pie-label" x="1076" y="201">30%</text>
    <text class="pie-label" x="1042" y="265">28%</text>
    <text class="pie-label" x="944" y="231">28%</text>
    <text class="pie-label" x="994" y="189">12%</text>
    <text class="pie-label outside" x="944" y="335">2%</text>
    <rect class="fill-red" x="978" y="352" width="18" height="13" rx="4"/>
    <rect class="fill-blue" x="978" y="377" width="18" height="13" rx="4"/>
    <rect class="fill-purple" x="978" y="402" width="18" height="13" rx="4"/>
    <rect class="fill-orange" x="978" y="428" width="18" height="13" rx="4"/>
    <rect class="fill-green" x="978" y="454" width="18" height="13" rx="4"/>
    <text class="legend-text" x="1001" y="364">Competitor 1</text>
    <text class="legend-text" x="1001" y="389">Competitor 2</text>
    <text class="legend-text" x="1001" y="414">Competitor 3</text>
    <text class="legend-text" x="1001" y="440">Competitor 4</text>
    <text class="legend-text" x="1001" y="466">Yours</text>
  </g>

  <!-- C. Visibility -->
  <g class="chart-visibility">
    <text class="panel-title" x="134" y="556">C. <tspan class="accent">Visibility</tspan></text>
    <text class="axis-small" x="43" y="521">Visibility</text>
    <path class="axis-line" d="M82 536 V853 H500"/>
    <g class="axis-text" text-anchor="end">
      <text x="66" y="856">0%</text><text x="66" y="825">10%</text><text x="66" y="793">20%</text>
      <text x="66" y="761">30%</text><text x="66" y="729">40%</text><text x="66" y="698">50%</text>
      <text x="66" y="666">60%</text><text x="66" y="634">70%</text><text x="66" y="603">80%</text>
      <text x="66" y="571">90%</text><text x="66" y="539">100%</text>
    </g>
    <g class="axis-small" text-anchor="middle">
      <text x="106" y="866">00</text><text x="122" y="866">01</text><text x="138" y="866">02</text>
      <text x="153" y="866">03</text><text x="169" y="866">04</text><text x="185" y="866">05</text>
      <text x="201" y="866">06</text><text x="217" y="866">07</text><text x="233" y="866">08</text>
      <text x="248" y="866">09</text><text x="264" y="866">10</text><text x="280" y="866">11</text>
      <text x="296" y="866">12</text><text x="312" y="866">13</text><text x="328" y="866">14</text>
      <text x="343" y="866">15</text><text x="359" y="866">16</text><text x="375" y="866">17</text>
      <text x="391" y="866">18</text><text x="407" y="866">19</text><text x="423" y="866">20</text>
      <text x="438" y="866">21</text><text x="454" y="866">22</text><text x="470" y="866">23</text>
      <text x="512" y="866">Hour</text>
      <text x="283" y="881">Day</text>
    </g>
    <polyline class="series series-yours" points="106,637.4 122,635.9 138,631.1 153,632.7 169,629.5 185,626.3 201,626.3 217,620 233,618.4 248,626.3 264,624.8 280,618.4 296,610.5 312,602.6 328,599.4 343,599.4 359,599.4 375,602.6 391,602.6 407,599.4 423,599.4 438,602.6 454,604.2 470,605.7"/>
    <polyline class="series series-c1" points="106,669.1 122,675.5 138,677.1 153,681.8 169,678.7 185,689.7 201,686.6 217,683.4 233,691.3 248,696.1 264,700.8 280,702.4 296,708.8 312,710.4 328,708.8 343,715.1 359,711.9 375,710.4 391,708.8 407,707.2 423,694.5 438,689.7 454,685 470,681.8"/>
    <polyline class="series series-c2" points="106,694.5 122,699.3 138,700.8 153,702.4 169,699.3 185,685 201,691.3 217,694.5 233,672.3 248,673.9 264,677.1 280,685 296,691.3 312,694.5 328,696.1 343,696.1 359,691.3 375,691.3 391,692.9 407,696.1 423,699.3 438,702.4 454,704 470,700.8"/>
    <rect class="fill-green" x="408" y="764" width="10" height="10"/>
    <rect class="fill-red" x="408" y="785" width="10" height="10"/>
    <rect class="fill-blue" x="408" y="805" width="10" height="10"/>
    <text class="legend-text" x="422" y="775">Your website</text>
    <text class="legend-text" x="422" y="796">Competitor 1</text>
    <text class="legend-text" x="422" y="816">Competitor 2</text>
  </g>

  <!-- D. Matrix -->
  <g class="chart-matrix">
    <text class="panel-title" x="836" y="570">D. <tspan class="accent">Matrix</tspan></text>
    <path class="axis-line" d="M660 533 V848 H1172"/>
    <g class="axis-small" text-anchor="end">
      <text x="654" y="851">0%</text><text x="654" y="820">10%</text><text x="654" y="788">20%</text>
      <text x="654" y="757">30%</text><text x="654" y="725">40%</text><text x="654" y="694">50%</text>
      <text x="654" y="662">60%</text><text x="654" y="631">70%</text><text x="654" y="599">80%</text>
      <text x="654" y="568">90%</text><text x="654" y="536">100%</text>
    </g>
    <rect class="fill-blue" x="699" y="545.6" width="20" height="302.4"/>
    <rect class="fill-green" x="721" y="577.1" width="20" height="270.9"/>
    <rect class="fill-red" x="742" y="627.5" width="20" height="220.5"/>
    <rect class="fill-blue" x="822" y="838.5" width="20" height="9.5"/>
    <rect class="fill-green" x="843" y="822.8" width="20" height="25.2"/>
    <rect class="fill-red" x="865" y="800.7" width="20" height="47.3"/>
    <rect class="fill-blue" x="944" y="844.8" width="20" height="3.2"/>
    <rect class="fill-green" x="966" y="832.2" width="20" height="15.8"/>
    <rect class="fill-red" x="988" y="822.8" width="20" height="25.2"/>
    <rect class="fill-green" x="1088" y="844.8" width="20" height="3.2"/>
    <rect class="fill-red" x="1110" y="826" width="20" height="22"/>
    <g class="axis-small" text-anchor="middle">
      <text x="709" y="540">96%</text><text x="731" y="572">86%</text><text x="752" y="622">70%</text>
      <text x="832" y="833">3%</text><text x="853" y="817">8%</text><text x="875" y="795">15%</text>
      <text x="954" y="839">1%</text><text x="976" y="827">5%</text><text x="998" y="817">8%</text>
      <text x="1076" y="842">0%</text><text x="1098" y="839">1%</text><text x="1120" y="820">7%</text>
      <text x="730" y="866">Classic</text><text x="853" y="866">Images</text>
      <text x="976" y="866">Video</text><text x="1098" y="866">Shopping</text>
    </g>
    <rect class="fill-green" x="1023" y="703" width="10" height="10"/>
    <rect class="fill-red" x="1023" y="724" width="10" height="10"/>
    <rect class="fill-blue" x="1023" y="745" width="10" height="10"/>
    <text class="legend-text" x="1037" y="714">Yours</text>
    <text class="legend-text" x="1037" y="735">Competitor 1</text>
    <text class="legend-text" x="1037" y="756">Competitor 2</text>
  </g>
</svg>
</body>
</html>
```